TRIVEL Corp Has New Logo Now Needs New Stationary

We just chose our new logo, and now we need a letterhead and envelope design. I would like both to be used via Microsoft Word so I can print both the letterhead and envelopes myself rather than having to the letterhead and envelopes produced by a printing firm. I has attached the new logo and spec sheet provided by the logo designer.

```html
<!DOCTYPE html>
<html lang="en">
<head>
<meta charset="utf-8">
<title>TRIVEL Corp Foundation – Stationery</title>
<link rel="stylesheet" href="https://fonts.googleapis.com/css2?family=Montserrat:wght@600&family=Open+Sans:wght@400&display=swap">
<style>
  :root {
    --backdrop: #e9e6e1;
    --paper: #ffffff;
    --paper-shade: #f3f3f3;
    --edge: #b9b9b9;
    --ink: #333333;
    --ink-soft: #555555;
    --brand-blue: #41ade1;
    --brand-green: #72b840;
  }
  * { box-sizing: border-box; margin: 0; padding: 0; }
  html, body { width: 1200px; height: 700px; overflow: hidden; }
  body {
    position: relative;
    background: var(--backdrop);
    font-family: "Open Sans", Arial, sans-serif;
    color: var(--ink);
  }

  /* ---------- shared brand block ---------- */
  .brand { position: absolute; }
  .brand-mark {
    width: 44px; height: 44px; border-radius: 50%;
    background: var(--brand-blue);
    margin: 0 auto 10px;
  }
  .brand-name {
    font-family: "Montserrat", Arial, sans-serif;
    font-weight: 600;
    color: var(--ink);
    line-height: 1;
    letter-spacing: -0.5px;
    white-space: nowrap;
  }
  .brand-sub {
    font-family: "Montserrat", Arial, sans-serif;
    font-weight: 600;
    color: var(--ink);
    text-align: center;
    letter-spacing: 3.4px;
    margin-top: 4px;
    font-size: 9px;
  }

  /* ---------- letterhead ---------- */
  .letterhead {
    position: absolute; left: 17px; top: 15px;
    width: 510px; height: 661px;
    background: var(--paper);
    box-shadow: 0 1px 3px rgba(0,0,0,.25);
    overflow: hidden;
  }
  .letterhead .brand { left: 8px; top: 16px; width: 178px; }
  .letterhead .brand-name { font-size: 27px; }

  .contact-list {
    position: absolute; left: 392px; top: 30px;
    list-style: none;
    border-left: 1px solid #cfcfcf;
    padding-left: 6px;
    font-size: 9.5px; line-height: 13px;
    color: var(--ink);
  }
  .contact-list li { display: flex; align-items: center; gap: 4px; }
  .contact-list svg { width: 8px; height: 8px; flex: none; }

  .letter-footer {
    position: absolute; left: 0; bottom: 0;
    width: 510px; height: 64px;
  }
  .letter-footer svg { position: absolute; inset: 0; }
  .letter-address {
    position: absolute; left: 59px; bottom: 18px;
    font-size: 9px; color: var(--paper);
  }

  /* ---------- envelopes ---------- */
  .envelope {
    position: absolute;
    width: 556px; height: 271px;
    background: var(--paper);
    border: 1px solid var(--edge);
    overflow: hidden;
  }
  .envelope-back { left: 617px; top: 45px; }
  .envelope-back .flap {
    position: absolute; left: 0; top: 0; width: 100%; height: 83px;
    background: var(--brand-blue);
    clip-path: polygon(0 0, 100% 0, 99% 100%, 1% 100%);
  }
  .envelope-back .flap-mark {
    position: absolute; left: 239px; top: 18px;
    width: 46px; height: 46px; border-radius: 50%;
    background: var(--paper);
  }

  .envelope-inside { left: 584px; top: 160px; }
  .envelope-inside .flap {
    position: absolute; left: 0; top: 0; width: 100%; height: 83px;
    background: var(--paper-shade);
    border-bottom: 1px solid #c9c9c9;
    clip-path: polygon(0 0, 100% 0, 98% 100%, 2% 100%);
  }
  .envelope-inside .flap-mark {
    position: absolute; left: 237px; top: 15px;
    width: 46px; height: 46px; border-radius: 50%;
    background: var(--brand-green);
  }

  .envelope-front { left: 549px; top: 292px; }
  .envelope-front .brand { left: 8px; top: 16px; width: 172px; }
  .envelope-front .brand-name { font-size: 25px; }
  .envelope-front .brand-mark { width: 40px; height: 40px; margin-bottom: 14px; }
  .return-address {
    position: absolute; left: 14px; top: 121px;
    font-size: 9.5px; color: var(--ink);
  }
  .envelope-footer {
    position: absolute; left: 0; bottom: 0; width: 100%; height: 62px;
  }
  .envelope-footer svg { position: absolute; inset: 0; }
  .envelope-web {
    position: absolute; left: 55px; bottom: 16px;
    font-size: 10px; letter-spacing: 2.4px; color: var(--paper);
  }
</style>
</head>
<body>

  <!-- Letterhead -->
  <section class="letterhead">
    <div class="brand">
      <div class="brand-mark"></div>
      <div class="brand-name">TRIVEL CORP</div>
      <div class="brand-sub">FOUNDATION</div>
    </div>

    <ul class="contact-list">
      <li>
        <svg viewBox="0 0 8 8"><circle cx="4" cy="4" r="3.5" fill="none" stroke="#41ade1"/><path d="M2.6 2.3 L3.4 2.3 L3.6 3.3 L3.1 3.7 Q3.8 4.7 4.5 5 L4.9 4.5 L5.8 4.7 L5.8 5.5 Q3 5.6 2.6 2.3Z" fill="#41ade1"/></svg>
        123-456-0789
      </li>
      <li>
        <svg viewBox="0 0 8 8"><rect x="2.3" y="0.5" width="3.4" height="7" rx="0.7" fill="#41ade1"/><rect x="2.9" y="1.3" width="2.2" height="4.4" fill="#fff"/></svg>
        123-456-0789
      </li>
      <li>
        <svg viewBox="0 0 8 8"><rect x="0.5" y="1.8" width="7" height="4.6" fill="#41ade1"/><path d="M0.5 1.8 L4 4.6 L7.5 1.8" fill="none" stroke="#fff" stroke-width="0.7"/></svg>
        info@trivelmail.com
      </li>
      <li>
        <svg viewBox="0 0 8 8"><circle cx="4" cy="4" r="3.5" fill="#41ade1"/><ellipse cx="4" cy="4" rx="1.5" ry="3.5" fill="none" stroke="#fff" stroke-width="0.5"/><line x1="0.5" y1="4" x2="7.5" y2="4" stroke="#fff" stroke-width="0.5"/></svg>
        www.trivelcorp.com
      </li>
    </ul>

    <footer class="letter-footer">
      <svg viewBox="0 0 510 64" preserveAspectRatio="none" aria-hidden="true">
        <path d="M0 34 C120 2 250 20 330 40 C400 56 460 40 510 16 L510 64 L0 64 Z" fill="var(--brand-green)"/>
        <path d="M0 38 C120 8 250 24 330 44 C400 60 460 44 510 22 L510 64 L0 64 Z" fill="var(--paper)"/>
        <path d="M0 41 C120 12 250 28 330 48 C400 63 460 48 510 26 L510 64 L0 64 Z" fill="var(--brand-blue)"/>
      </svg>
      <p class="letter-address">Street Name, City Name, State Zip Code</p>
    </footer>
  </section>

  <!-- Envelope, back with blue flap -->
  <section class="envelope envelope-back">
    <div class="flap"><div class="flap-mark"></div></div>
  </section>

  <!-- Envelope, back with open flap -->
  <section class="envelope envelope-inside">
    <div class="flap"><div class="flap-mark"></div></div>
  </section>

  <!-- Envelope, front -->
  <section class="envelope envelope-front">
    <div class="brand">
      <div class="brand-mark"></div>
      <div class="brand-name">TRIVEL CORP</div>
      <div class="brand-sub">FOUNDATION</div>
    </div>
    <p class="return-address">Street Name, City Name, State Zip Code</p>
    <footer class="envelope-footer">
      <svg viewBox="0 0 556 62" preserveAspectRatio="none" aria-hidden="true">
        <path d="M0 20 C120 2 230 14 320 36 C400 52 480 40 556 8 L556 62 L0 62 Z" fill="var(--brand-green)"/>
        <path d="M0 24 C120 7 230 19 320 40 C400 56 480 44 556 13 L556 62 L0 62 Z" fill="var(--paper)"/>
        <path d="M0 27 C120 11 230 23 320 44 C400 59 480 48 556 17 L556 62 L0 62 Z" fill="var(--brand-blue)"/>
      </svg>
      <p class="envelope-web">www.trivelcorp.com</p>
    </footer>
  </section>

</body>
</html>
```